Need new sign at entrance for new fruit and vegetable wholesaler in market. Main vegetables sold are
Broccoli , Cauliflower , cabbage , capsicum , tomatoes , lettuce .
Business name is Tenby Crop
I have included examples of other designs and a sketch of suggested layout.
Business

```html
<!DOCTYPE html>
<html lang="en">
<head>
<meta charset="utf-8">
<title>Tenby Crop – Entrance Sign</title>
<link href="https://fonts.googleapis.com/css2?family=Arvo:wght@700&family=Questrial&display=swap" rel="stylesheet">
<style>
  :root {
    --page: #ffffff;
    --lime-light: #e4ef8a;
    --lime: #c5de47;
    --lime-deep: #9cc62c;
    --ink: #111111;
    --accent-red: #e0262a;
    --veg-green: #6fb84a;
    --veg-red: #e0402e;
    --veg-yellow: #f5b820;
  }
  html, body {
    margin: 0;
    padding: 0;
    width: 1200px;
    height: 1000px;
    overflow: hidden;
    background: var(--page);
  }
  .canvas {
    position: relative;
    width: 1200px;
    height: 1000px;
  }
  .sign {
    position: absolute;
    left: 50px;
    top: 396px;
    width: 1098px;
    height: 207px;
    overflow: hidden;
    background:
      radial-gradient(ellipse 420px 260px at 640px 60px, var(--lime-light) 0%, rgba(228,239,138,0) 70%),
      linear-gradient(90deg, var(--lime-deep) 0%, var(--lime) 30%, var(--lime) 75%, var(--lime-deep) 100%);
  }
  .produce-illustration {
    position: absolute;
    left: 12px;
    top: 26px;
    width: 432px;
    height: 172px;
    border-radius: 60px 70px 50px 40px;
    background: linear-gradient(90deg,
      #5fb3a0 0%, #7cc4a4 18%, #f3f1e2 30%, var(--veg-green) 48%,
      var(--veg-red) 62%, var(--veg-green) 74%, var(--veg-yellow) 88%, #f08a1c 100%);
    opacity: 0.9;
  }
  .stall-location {
    position: absolute;
    left: 170px;
    top: 11px;
    font-family: "Questrial", sans-serif;
    font-size: 18px;
    color: var(--ink);
    margin: 0;
  }
  .brand-block {
    position: absolute;
    left: 430px;
    top: 20px;
    width: 660px;
    transform: rotate(-6deg);
    transform-origin: left bottom;
  }
  .web-address {
    margin: 0 0 -14px 95px;
    font-family: "Questrial", sans-serif;
    font-size: 21px;
    color: var(--accent-red);
  }
  .brand-name {
    margin: 0;
    font-family: "Arvo", serif;
    font-weight: 700;
    font-size: 100px;
    letter-spacing: -3px;
    line-height: 1.25;
    color: var(--ink);
    white-space: nowrap;
  }
  .contact-lines {
    position: absolute;
    right: 26px;
    top: 132px;
    margin: 0;
    font-family: "Questrial", sans-serif;
    font-size: 19px;
    line-height: 23px;
    color: var(--accent-red);
    text-align: right;
    transform: rotate(-5deg);
    transform-origin: right bottom;
  }
  .contact-lines .label { margin-right: 14px; }
</style>
</head>
<body>
<div class="canvas">
  <section class="sign">
    <div class="produce-illustration" role="img" aria-label="Illustration of cabbage, cauliflower, lettuce, tomatoes, broccoli and capsicums in a row"></div>
    <p class="stall-location">Stand 74&nbsp; C Shed</p>
    <div class="brand-block">
      <p class="web-address">tenbycrop.com.au</p>
      <h1 class="brand-name">Tenby Crop</h1>
    </div>
    <p class="contact-lines">
      <span class="label">Phone:</span>02 5550 1928<br>
      <span class="label">Fax:</span>02 5550 1928
    </p>
  </section>
</div>
</body>
</html>
```